Letterhead Design Project

We need s letterhead design for a Non Governmental Organization called 'VELMORIX'. We are into promoting innovative agricultural practices to support food security, poverty alleviation, agrobusiness and wealth creation under environmentally sound practices. We also focus on advocacy for agriculture as the engine of growth of economies in Sub-Saharan Africa and Nigeria in particular. We love the green colour and orange or yellow. The final design should communicate agriculture as source of economic growth, health, good environment and peace.
Updates

Reason: I am out of office for next week and may not have access to the internet.

Industry/Entity Type

Agriculture

```html
<!DOCTYPE html>
<html lang="en">
<head>
<meta charset="utf-8">
<title>VELMORIX Stationery</title>
<link rel="stylesheet" href="https://fonts.googleapis.com/css2?family=Josefin+Sans:wght@400&family=Arimo:wght@400;700&display=swap">
<style>
  :root {
    --backdrop: #a8a8a8;
    --paper: #fbfbfb;
    --paper-band: #efefef;
    --brand-green: #5f9e2c;
    --brand-lime: #c9dc3a;
    --envelope-green: #0b9a3e;
    --window-grey: #a4a4a4;
    --ink: #333333;
    --ink-soft: #555555;
  }
  * { margin: 0; padding: 0; box-sizing: border-box; }
  html, body { width: 1200px; height: 797px; overflow: hidden; }
  body {
    position: relative;
    background: var(--backdrop);
    font-family: "Arimo", Arial, sans-serif;
    color: var(--ink);
  }

  .brand {
    position: absolute;
    display: flex;
    align-items: center;
    font-family: "Josefin Sans", sans-serif;
    font-weight: 400;
    color: var(--brand-green);
    white-space: nowrap;
  }
  .brand-dot {
    border-radius: 50%;
    background: var(--brand-lime);
    flex: none;
  }

  .brand--hero { left: 372px; top: 30px; font-size: 46px; letter-spacing: 12px; gap: 22px; }
  .brand--hero .brand-dot { width: 84px; height: 84px; }

  /* Letterhead */
  .letterhead {
    position: absolute;
    left: 66px; top: 168px;
    width: 502px; height: 610px;
    background: var(--paper);
  }
  .letterhead-rail {
    position: absolute;
    left: 0; top: 0;
    width: 30px; height: 580px;
    background: var(--paper-band);
    border-bottom-right-radius: 28px;
  }
  .brand--letter { left: 64px; top: 66px; font-size: 19px; letter-spacing: 5px; gap: 10px; }
  .brand--letter .brand-dot { width: 40px; height: 40px; }

  .letter-body {
    position: absolute;
    left: 60px; top: 146px;
    width: 415px;
    font-size: 6.8px;
    line-height: 1.5;
    color: var(--ink-soft);
  }
  .letter-date { font-size: 9.5px; color: var(--ink); }
  .letter-subject { font-size: 9.5px; font-weight: 700; text-decoration: underline; color: var(--ink); margin-bottom: 9px; }
  .letter-body p + p { margin-top: 9px; }

  .letter-closing {
    position: absolute;
    left: 60px; top: 458px;
    font-size: 6.8px;
    color: var(--ink);
  }
  .letter-signature {
    position: absolute;
    left: 60px; top: 526px;
    width: 115px;
    border-top: 1px solid #888;
    padding-top: 8px;
    font-size: 7px;
    line-height: 1.4;
  }
  .letter-signature strong { display: block; }

  /* Envelope front */
  .envelope-front {
    position: absolute;
    left: 602px; top: 186px;
    width: 544px; height: 258px;
    background: var(--paper);
  }
  .brand--envelope { left: 56px; top: 36px; font-size: 22px; letter-spacing: 6px; gap: 12px; }
  .brand--envelope .brand-dot { width: 46px; height: 46px; }
  .envelope-window {
    position: absolute;
    left: 54px; top: 119px;
    width: 228px; height: 80px;
    background: var(--window-grey);
    border-radius: 3px;
  }

  /* Envelope back */
  .envelope-back {
    position: absolute;
    left: 602px; top: 510px;
    width: 544px; height: 258px;
    background: var(--envelope-green);
  }
  .envelope-flap { position: absolute; left: 0; top: 0; width: 544px; height: 58px; }
</style>
</head>
<body>

  <div class="brand brand--hero"><span class="brand-dot"></span>VELMORIX</div>

  <article class="letterhead">
    <div class="letterhead-rail"></div>
    <div class="brand brand--letter"><span class="brand-dot"></span>VELMORIX</div>

    <div class="letter-body">
      <p class="letter-date">Date: 23 November 2013</p>
      <p class="letter-subject">RE: Lorem ipsum dolor sit amet</p>
      <p>Lorem ipsum dolor sit amet, consectetuer adipiscing elit, sed diam nonummy nibh euismod tincidunt ut laoreet dolore magna aliquam erat volutpat. Ut wisi enim ad minim veniam, quis nostrud exerci tation ullamcorper suscipit lobortis nisl ut aliquip ex ea commodo consequat.</p>
      <p>Lorem ipsum dolor sit amet, consectetuer adipiscing elit, sed diam nonummy nibh euismod tincidunt ut laoreet dolore magna aliquam erat volutpat. Ut wisi enim ad minim veniam, quis nostrud exerci tation ullamcorper suscipit lobortis nisl ut aliquip ex ea commodo consequat. Lorem ipsum dolor sit amet, consectetuer adipiscing elit, sed diam nonummy nibh euismod tincidunt ut laoreet dolore magna aliquam erat volutpat.</p>
      <p>Lorem ipsum dolor sit amet, consectetuer adipiscing elit, sed diam nonummy nibh euismod tincidunt ut laoreet dolore magna aliquam erat volutpat. Ut wisi enim ad minim veniam, quis nostrud exerci tation ullamcorper suscipit lobortis nisl ut aliquip ex ea commodo consequat. Lorem ipsum dolor sit amet, consectetuer adipiscing elit, sed diam nonummy nibh euismod tincidunt ut laoreet dolore magna aliquam erat volutpat. Ut wisi enim ad minim veniam, quis nostrud exerci tation ullamcorper suscipit lobortis nisl ut aliquip ex ea commodo consequat.</p>
      <p>Lorem ipsum dolor sit amet, consectetuer adipiscing elit, sed diam nonummy nibh euismod tincidunt ut laoreet dolore magna aliquam erat volutpat.</p>
    </div>

    <p class="letter-closing">Yours sincerely,</p>
    <div class="letter-signature"><strong>JOHN DOE</strong>Senior manager</div>
  </article>

  <section class="envelope-front">
    <div class="brand brand--envelope"><span class="brand-dot"></span>VELMORIX</div>
    <div class="envelope-window"></div>
  </section>

  <section class="envelope-back">
    <svg class="envelope-flap" viewBox="0 0 544 58" aria-hidden="true">
      <polygon points="0,0 544,0 532,50 524,58 20,58 12,50" fill="#fbfbfb"/>
    </svg>
  </section>

</body>
</html>
```